Lortexa CBD oil tincture bottle product label design

I need a product label designed for a CBD hemp oil tincture bottle. The label size should be 34mm x 62mm narrow edge leading. Format wise, a high quality jpeg or pdf.

The product is a food supplement for health benefits. The colour scheme is green/gold. The logo and all of the information on the attached label needs to be included however the image, and design/layout can be changed. I do like the label that's attached Id just like others to compare.

Target Market(s)

health/supplement market

Requirements
Must have
• Green/gold theme

```html
<!DOCTYPE html>
<html lang="en">
<head>
<meta charset="utf-8">
<title>Lortexa Full Spectrum Hemp Oil – Label</title>
<link rel="stylesheet" href="https://fonts.googleapis.com/css2?family=Oswald:wght@300;400;600&family=Josefin+Sans:wght@300;600;700&family=Arvo:wght@700&display=swap">
<style>
  :root {
    --stage: #e4e4e4;
    --green-deep: #0f3a1a;
    --green-mid: #1f7a22;
    --green-bright: #3fc73a;
    --band-green: #0d9a3f;
    --gold-light: #f5dd7a;
    --gold: #d9b23c;
    --gold-dark: #a9821c;
    --ink-light: #ffffff;
  }
  * { box-sizing: border-box; margin: 0; padding: 0; }
  html, body { width: 1200px; height: 900px; overflow: hidden; }
  body { background: var(--stage); position: relative; }

  .label {
    position: absolute; left: 50px; top: 149px;
    width: 1100px; height: 602px; overflow: hidden;
    background: var(--green-deep);
    color: var(--ink-light);
    font-family: "Oswald", sans-serif;
  }
  .label__artwork {
    position: absolute; inset: 0;
    background:
      radial-gradient(ellipse 34% 70% at 50% 48%, rgba(9,40,16,.85) 0%, rgba(9,40,16,.6) 45%, rgba(9,40,16,0) 75%),
      radial-gradient(ellipse 60% 90% at 50% 45%, var(--green-bright) 0%, var(--green-mid) 45%, var(--green-deep) 85%);
  }

  .info { position: absolute; font-size: 22px; line-height: 31px; font-weight: 300; letter-spacing: -.3px; }
  .info h2 { font-size: 24px; font-weight: 600; line-height: 31px; letter-spacing: -.3px; }
  .info--contains { left: 24px; top: 38px; width: 300px; }
  .info--distributor { left: 24px; top: 355px; }
  .info--usage { left: 768px; top: 38px; width: 310px; }
  .info--storage { left: 768px; top: 291px; width: 310px; }

  .divider { position: absolute; left: 24px; top: 330px; width: 288px; height: 1px; background: rgba(255,255,255,.7); }

  .badge {
    position: absolute; top: 450px; width: 78px; height: 78px;
    border-radius: 50%; border: 3px solid var(--ink-light);
    background: rgba(255,255,255,.12);
  }
  .badge--first { left: 25px; }
  .badge--second { left: 119px; }

  .tracking { position: absolute; left: 768px; font-size: 22px; font-weight: 300; }
  .tracking__row { display: flex; align-items: center; height: 33px; }
  .tracking__label { width: 69px; }
  .tracking__field { width: 218px; height: 27px; border-radius: 14px; background: var(--ink-light); }

  .brand {
    position: absolute; left: 0; width: 1100px; top: 185px; text-align: center;
    font-family: "Josefin Sans", sans-serif; font-weight: 300;
    font-size: 54px; letter-spacing: 9px; color: var(--ink-light);
  }

  .title-frame { position: absolute; left: 0; top: 0; }

  .centre-line { position: absolute; left: 0; width: 1100px; text-align: center; }
  .spectrum {
    top: 265px; font-family: "Josefin Sans", sans-serif; font-weight: 700;
    font-size: 29px; letter-spacing: 6px; color: var(--ink-light);
  }
  .product-name {
    top: 300px; font-family: "Arvo", serif; font-weight: 700; font-size: 72px;
    color: var(--gold-light);
    background: linear-gradient(180deg, var(--gold-light), var(--gold) 55%, var(--gold-dark));
    -webkit-background-clip: text; background-clip: text; -webkit-text-fill-color: transparent;
  }
  .strength {
    top: 401px; font-family: "Josefin Sans", sans-serif; font-weight: 600;
    font-size: 44px; color: var(--ink-light);
  }
  .extraction {
    top: 452px; font-family: "Josefin Sans", sans-serif; font-weight: 600;
    font-size: 42px; color: var(--gold); letter-spacing: 1px;
  }
  .extraction sup { font-size: 22px; }

  .volume-band { position: absolute; left: 0; bottom: 0; width: 1100px; height: 46px; background: var(--band-green); }
  .volume-seal {
    position: absolute; left: 389px; top: 517px; width: 322px; height: 170px; border-radius: 50%;
    background: linear-gradient(90deg, var(--gold-dark), var(--gold-light) 50%, var(--gold-dark));
  }
  .volume {
    top: 556px; font-family: "Josefin Sans", sans-serif; font-weight: 600;
    font-size: 28px; color: var(--green-deep);
  }
</style>
</head>
<body>
  <section class="label">
    <div class="label__artwork" role="img" aria-label="Bright green hemp fibre burst behind a dark silhouette of a human figure"></div>

    <div class="info info--contains">
      <h2>CONTAINS:</h2>
      <p>10ml organic certified hemp oil<br>from hemp (Cannabis sativa)<br>Supercritical CO2 extracted.<br>Hemp seed oil (77%)<br>hemo extract (23%)<br>500mg CBD+CBDa.<br>Approximetaly 2mg CBDper drop</p>
    </div>
    <div class="divider"></div>
    <div class="info info--distributor">
      <h2>DISTRIBUTED BY:</h2>
      <p>LORTEXA Ltd.<br>Product of the EU</p>
    </div>
    <div class="badge badge--first"></div>
    <div class="badge badge--second"></div>

    <div class="info info--usage">
      <h2>RECOMENDED USE:</h2>
      <p>As food supplement, use twice daily. Place 10-15 drops under the tongue.. Hold for 60 sec., then swallow. Do not exceed 200mg/day<br>Shake before use.</p>
    </div>
    <div class="info info--storage">
      <h2>STORAGE:</h2>
      <p>Store away from sunlight, heat &amp; humidity.<br>Keep out from reach of children</p>
    </div>
    <div class="tracking" style="top:450px;">
      <div class="tracking__row"><span class="tracking__label">batch:</span><span class="tracking__field"></span></div>
      <div class="tracking__row"><span class="tracking__label">use by:</span><span class="tracking__field"></span></div>
    </div>

    <div class="brand">LORTEXA</div>

    <svg class="title-frame" width="1100" height="602" viewBox="0 0 1100 602" aria-hidden="true">
      <path d="M372 270 H354 V429 H438 M662 429 H745 V270 H727" fill="none" stroke="#d9b23c" stroke-width="2.5"/>
    </svg>
    <div class="centre-line spectrum">FULL SPECTRUM</div>
    <div class="centre-line product-name">Hemp Oil</div>
    <div class="centre-line strength">5% CBD</div>
    <div class="centre-line extraction">CO<sup>2</sup> EXTRACTED</div>

    <div class="volume-band"></div>
    <div class="volume-seal"></div>
    <div class="centre-line volume">10ML [0.33 FLOZ]</div>
  </section>
</body>
</html>
```